Business Card Design

we specialise in supply of custom uniforms - teamwear to Schools and sporting clubs, see our website: www.kestrelkitworks.com.au, our main corporate colour is black and white, with small amount of gold/yellow

Industry/Entity Type

Business

Contact Information for Business Card

Kestrel Kit Works
Rowan Petrakis
Ph 03 6219 8805
Mobile 0418 262 740
email: rowan@kestrelkitworks.com.au
www.kestrelkitworks.com.au
like us on flockly

Requirements
Must have
• modern look & feel

```html
<!DOCTYPE html>
<html lang="en">
<head>
<meta charset="utf-8">
<title>Kestrel Kit Works — Business Card</title>
<link href="https://fonts.googleapis.com/css2?family=Josefin+Sans:wght@300;400;700&display=swap" rel="stylesheet">
<style>
  :root {
    --stage: #e4e4e4;
    --card: #1b1918;
    --card-edge: #121110;
    --white: #ffffff;
    --text-soft: #dcdcdc;
    --gold: #e8c83a;
  }
  * { box-sizing: border-box; margin: 0; padding: 0; }
  html, body {
    width: 1200px; height: 900px; overflow: hidden;
    background: var(--stage);
    font-family: "Josefin Sans", sans-serif;
  }
  .canvas {
    position: relative; width: 1200px; height: 900px;
    display: flex; flex-direction: column; align-items: center;
    justify-content: center; gap: 50px;
  }
  .card {
    position: relative; width: 700px; height: 400px;
    background: var(--card);
    border-bottom: 8px solid var(--gold);
    box-shadow: 0 10px 30px rgba(0,0,0,.25);
    color: var(--white);
  }
  /* Front */
  .card-front { display: flex; align-items: center; justify-content: center; }
  .brand { display: flex; align-items: center; gap: 18px; }
  .brand-dot { width: 26px; height: 26px; border-radius: 50%; background: var(--white); flex: none; }
  .brand-name { font-weight: 700; font-size: 46px; color: var(--white); letter-spacing: .5px; }
  /* Back */
  .card-back { padding: 48px 44px; display: flex; gap: 40px; }
  .card-back .brand { align-self: flex-start; gap: 10px; }
  .card-back .brand-dot { width: 16px; height: 16px; }
  .card-back .brand-name { font-size: 24px; }
  .contact { margin-top: 4px; }
  .person-name {
    font-weight: 400; font-size: 32px; letter-spacing: 5px;
    color: var(--white); margin-bottom: 18px;
  }
  .contact-list { list-style: none; }
  .contact-list li {
    display: flex; align-items: center; gap: 10px;
    font-weight: 300; font-size: 15.5px; letter-spacing: 2px;
    color: var(--text-soft); height: 27px;
  }
  .icon { width: 18px; height: 18px; flex: none; }
</style>
</head>
<body>
<main class="canvas">

  <section class="card card-front">
    <div class="brand">
      <span class="brand-dot"></span>
      <span class="brand-name">Kestrel Kit Works</span>
    </div>
  </section>

  <section class="card card-back">
    <div class="brand">
      <span class="brand-dot"></span>
      <span class="brand-name">Kestrel Kit Works</span>
    </div>
    <div class="contact">
      <h1 class="person-name">Rowan Petrakis</h1>
      <ul class="contact-list">
        <li>
          <svg class="icon" viewBox="0 0 18 18"><circle cx="9" cy="9" r="9" fill="var(--gold)"/><path d="M5.5 6.5c0 3 3 6 6 6l1-1.5-1.8-1-1 .7c-1-.5-1.9-1.4-2.4-2.4l.7-1-1-1.8z" fill="var(--card)"/></svg>
          phone: 03 6219 8805
        </li>
        <li>
          <svg class="icon" viewBox="0 0 18 18"><circle cx="9" cy="9" r="9" fill="var(--gold)"/><rect x="6.5" y="4.5" width="5" height="9" rx="1" fill="var(--card)"/></svg>
          mobile: 0418 262 740
        </li>
        <li>
          <svg class="icon" viewBox="0 0 18 18"><circle cx="9" cy="9" r="9" fill="var(--gold)"/><rect x="4.5" y="6" width="9" height="6.5" fill="var(--card)"/><path d="M4.5 6l4.5 3.5L13.5 6" stroke="var(--gold)" stroke-width="1" fill="none"/></svg>
          email: rowan@kestrelkitworks.com.au
        </li>
        <li>
          <svg class="icon" viewBox="0 0 18 18"><circle cx="9" cy="9" r="9" fill="var(--gold)"/><circle cx="9" cy="9" r="4.8" fill="none" stroke="var(--card)" stroke-width="1.2"/><ellipse cx="9" cy="9" rx="2" ry="4.8" fill="none" stroke="var(--card)" stroke-width="1"/><line x1="4.2" y1="9" x2="13.8" y2="9" stroke="var(--card)" stroke-width="1"/></svg>
          web: www.kestrelkitworks.com.au
        </li>
        <li>
          <svg class="icon" viewBox="0 0 18 18"><circle cx="9" cy="9" r="9" fill="var(--gold)"/></svg>
          like us on flockly
        </li>
      </ul>
    </div>
  </section>

</main>
</body>
</html>
```